Chimney Service company needs new business card design

We need a updated business card with our new logo added. We provide a full range of chimney services throughout Vermont and New Hampshire. The business card will be one sided and color. Attached is our current business card another document showing all the information we would like on the card.
We dont like a lot of flashy colors.... here is a link to our website to get an idea of our branding www.flueguardianvt.example

Target Market(s)

homeowners

Industry/Entity Type

Business

Contact Information for Business Card

See attached sheet for content.

Font styles to use
Serif
Sans Serif

Requirements
Must have
• all information provided on separate sheet
Should not have
• Additional information that may clogg up design

```html
<!DOCTYPE html>
<html lang="en">
<head>
<meta charset="utf-8">
<title>Flue Guardian — Business Card</title>
<link rel="stylesheet" href="https://fonts.googleapis.com/css2?family=Cinzel:wght@400;500&family=Montserrat:wght@400;500&display=swap">
<style>
  :root {
    --page: #e9e7e3;
    --card: #fbfbfa;
    --ink: #3c3c3c;
    --ink-soft: #5a5a5a;
    --rule: #8a8a8a;
    --brand-red: #9e1b21;
    --band-dark: #2f2f2f;
  }
  * { box-sizing: border-box; margin: 0; padding: 0; }
  html, body {
    width: 1200px; height: 1022px; overflow: hidden;
    background: var(--page);
  }
  .business-card {
    position: absolute;
    left: 75px; top: 211px;
    width: 1050px; height: 600px;
    background: var(--card);
    box-shadow: 0 10px 30px rgba(0,0,0,.18);
    overflow: hidden;
  }
  .brand {
    position: absolute; left: 70px; top: 70px;
    display: flex; align-items: center; gap: 30px;
  }
  .brand-square {
    width: 120px; height: 120px;
    background: var(--ink);
  }
  .brand-text { display: flex; flex-direction: column; }
  .brand-name {
    font-family: "Cinzel", serif;
    font-size: 50px; font-weight: 400;
    color: var(--ink); letter-spacing: 2px;
    padding-bottom: 6px;
    border-bottom: 2px solid var(--rule);
  }
  .brand-year {
    display: flex; align-items: center; gap: 14px;
    margin-top: 8px;
    font-family: "Cinzel", serif;
    font-size: 20px; color: var(--ink-soft); letter-spacing: 3px;
  }
  .brand-year::before {
    content: ""; width: 130px; height: 2px; background: var(--rule);
  }
  .service-list {
    position: absolute; left: 80px; top: 290px;
    list-style: none;
    font-family: "Montserrat", sans-serif;
    font-size: 25px; line-height: 46px;
    color: var(--ink-soft); letter-spacing: 0.5px;
    text-transform: uppercase;
  }
  .service-list li::before, .bullet {
    content: ""; display: inline-block;
    width: 10px; height: 10px; border-radius: 50%;
    background: var(--brand-red);
    margin: 0 14px 4px 0; vertical-align: middle;
  }
  .bullet { margin: 0 12px 4px 12px; }
  .contact {
    position: absolute; left: 640px; top: 395px;
    list-style: none;
    font-family: "Montserrat", sans-serif;
    font-size: 24px; line-height: 44px;
    color: var(--ink);
  }
  .contact li { display: flex; align-items: center; gap: 14px; }
  .contact svg { width: 20px; height: 20px; flex: none; }
  .card-band {
    position: absolute; left: 0; bottom: 0;
    width: 100%; height: 26px; display: flex;
  }
  .card-band .band-red { flex: 0 0 62%; background: var(--brand-red); }
  .card-band .band-dark { flex: 1; background: var(--band-dark); }
</style>
</head>
<body>
  <section class="business-card">
    <div class="brand">
      <div class="brand-square"></div>
      <div class="brand-text">
        <span class="brand-name">Flue Guardian</span>
        <span class="brand-year">INC 1989</span>
      </div>
    </div>

    <ul class="service-list">
      <li>Full Masonry Services</li>
      <li>Historic Chimney Restoration</li>
      <li>Stainless Steel Liners</li>
      <li>Fully Certified Chimney Sweep</li>
      <li>Fully Insured<span class="bullet"></span>Free Estimates</li>
    </ul>

    <ul class="contact">
      <li>
        <svg viewBox="0 0 20 20" aria-hidden="true"><path d="M5 2l3 4-2 2c1 2.5 3.5 5 6 6l2-2 4 3-2 3C8 18 2 12 2 4z" fill="var(--brand-red)"/></svg>
        802-555-0142
      </li>
      <li>
        <svg viewBox="0 0 20 20" aria-hidden="true"><rect x="2" y="4" width="16" height="12" fill="none" stroke="var(--brand-red)" stroke-width="2"/><path d="M2 4l8 7 8-7" fill="none" stroke="var(--brand-red)" stroke-width="2"/></svg>
        info@flueguardianvt.example
      </li>
      <li>
        <svg viewBox="0 0 20 20" aria-hidden="true"><circle cx="10" cy="10" r="8" fill="none" stroke="var(--brand-red)" stroke-width="2"/><ellipse cx="10" cy="10" rx="3.5" ry="8" fill="none" stroke="var(--brand-red)" stroke-width="1.6"/><path d="M2 10h16" stroke="var(--brand-red)" stroke-width="1.6"/></svg>
        www.flueguardianvt.example
      </li>
    </ul>

    <div class="card-band"><span class="band-red"></span><span class="band-dark"></span></div>
  </section>
</body>
</html>
```